Table talker for waiter rating service in restaurant

- Create a 3 sided table tent card to let restaurant customers know that they can rate their waiter's quality of service.

Layout
Divide an A4 page down the vertical i.e. 2 per A4 page. See template attached which shows the fold and cut lines.

Design
I want to show that the customer can rate their waiter's quality of service and win a free meal. The emphasis is NOT on the Plumo brand itself.
The table tents will be used at different restaurants so they have to be generic i.e. no pictures of a specific type of food i.e. italian. Possibly use multiple colors. Use images of food though.
Sides 1 and 2 need to be fun and exciting.
Side 3 needs to be very clear and easy to read. People are dumb.

Side 1
Rate your waiter and
Stand a chance to
Win a FREE meal for 2.

Side 2
We love our customers and want to hear from you.
Good or bad, we want to know.
P.S. It's 100% anonymous.

Side 3
Rate your waiter:
SMS your waiter's badge number and score out of 10 to 48216
Example: 99812 9
P.S. We hate spam. You will not be added to any mailing list.

Smaller along bottom edges
Terms and conditions apply. R3 per SMS. Brought to you by plumo.co.za (can also include small plumo logo)

I have changed the brief slightly. Please have a look. The design should let restaurant customer know that they can rate a waiter and not focus on the Plumo brand

Target Market(s)

Restaurant customers

Industry/Entity Type

Restaurant

Requirements
Nice to have
• Image of food or drink on the win page (side 1)
Small plumo logo at bottom of design
Should not have
• Plumo logo as focal point

```html
<!DOCTYPE html>
<html lang="en">
<head>
<meta charset="utf-8">
<title>Rate Your Waiter – Table Tent</title>
<link rel="stylesheet" href="https://fonts.googleapis.com/css2?family=Cinzel:wght@700;900&family=Kaushan+Script&family=Passion+One:wght@700&family=Tinos:wght@700&display=swap">
<style>
  :root {
    --green-light: #7cc142;
    --green: #4f9a2e;
    --green-dark: #2c5d1c;
    --orange-light: #fbc514;
    --orange: #f0a11c;
    --orange-dark: #b5661a;
    --paper: #f4f2f0;
    --brown: #3b1b16;
    --red: #c4202b;
    --red-dark: #7c0f14;
    --red-deep: #5e0a0e;
    --yellow: #f2ee2e;
    --lettuce: #5e9a3a;
    --white: #ffffff;
  }
  * { margin: 0; padding: 0; box-sizing: border-box; }
  html, body { width: 1200px; height: 848px; overflow: hidden; background: var(--white); }
  .tent { position: relative; width: 1200px; height: 848px; overflow: hidden; font-family: "Tinos", serif; }

  .side { position: absolute; top: 0; height: 848px; }
  .side--win {
    left: 0; width: 403px;
    background: radial-gradient(ellipse at 50% 20%, var(--green-light), var(--green) 55%, #3f8425);
    border: 8px solid var(--green-dark);
  }
  .side--hear {
    left: 403px; width: 400px;
    background: radial-gradient(ellipse at 45% 10%, var(--orange-light), var(--orange) 70%);
    border: 6px solid var(--orange-dark);
    outline: 1px solid #e8b86a; outline-offset: -12px;
  }
  .side--rate {
    left: 803px; width: 397px;
    background: var(--paper);
    border: 8px solid var(--brown);
  }
  .side--rate::after {
    content: ""; position: absolute; inset: 3px;
    border: 1px dotted #b9a7a2;
  }

  /* Side 1 */
  .win-block {
    position: absolute; left: 30px; top: 205px; width: 340px;
    transform: rotate(-8deg); text-align: center; color: var(--white);
  }
  .win-emblem {
    position: absolute; left: 60px; top: 70px; width: 220px; height: 150px;
    border-radius: 50%;
    background: radial-gradient(circle, rgba(90,40,30,.75), rgba(60,30,20,.35) 70%, transparent 72%);
  }
  .win-greens {
    position: absolute; width: 80px; height: 50px; border-radius: 50%;
    background: radial-gradient(circle, #8fcf5a, var(--lettuce));
  }
  .win-greens--left { left: 20px; top: 185px; }
  .win-greens--right { left: 250px; top: 140px; }
  .win-lead { position: relative; font-family: "Cinzel", serif; font-weight: 900; font-size: 21px; letter-spacing: .5px; text-shadow: 1px 2px 2px rgba(0,0,0,.5); }
  .win-chance { position: relative; font-family: "Kaushan Script", cursive; font-size: 38px; line-height: 1; margin-top: 2px; text-shadow: 2px 2px 2px rgba(0,0,0,.5); }
  .win-big { position: relative; font-family: "Passion One", sans-serif; font-weight: 700; font-size: 120px; line-height: .85; color: var(--yellow); text-shadow: 0 0 18px rgba(255,255,120,.6), 3px 4px 2px rgba(60,30,0,.6); }
  .win-cloche { position: absolute; left: 262px; top: 105px; width: 58px; height: 42px; }
  .win-meal {
    position: relative; display: inline-block; margin-top: 8px;
    font-family: "Cinzel", serif; font-weight: 900; font-size: 36px; line-height: 1;
    padding: 4px 10px; background: var(--red-dark); border-top: 2px solid #e6d6b0; border-bottom: 2px solid #e6d6b0;
  }
  .win-for { position: relative; font-family: "Kaushan Script", cursive; font-size: 44px; line-height: 1.2; text-shadow: 2px 2px 2px rgba(0,0,0,.4); }

  /* Side 2 */
  .hear-intro { position: absolute; left: 47px; top: 238px; color: var(--white); font-size: 17px; line-height: 1.3; }
  .hear-headline { position: absolute; left: 40px; top: 290px; color: var(--white); font-family: "Kaushan Script", cursive; font-size: 36px; line-height: 1; text-shadow: 2px 2px 3px rgba(150,80,0,.5); }
  .hear-headline span { display: block; padding-left: 20px; }
  .hear-ps { position: absolute; left: 48px; top: 420px; color: var(--white); font-family: "Kaushan Script", cursive; font-size: 17px; }
  .hear-ps small { font-family: "Tinos", serif; font-size: 12px; margin-right: 6px; }

  /* Side 3 */
  .rate-medal { position: absolute; left: 138px; top: 66px; width: 124px; height: 150px; }
  .rate-title {
    position: absolute; left: 27px; top: 240px; width: 232px;
    font-family: "Cinzel", serif; font-weight: 900; font-size: 21px; color: var(--brown);
    border-top: 2px dotted var(--brown); border-bottom: 2px dotted var(--brown); padding: 1px 0 0;
  }
  .rate-copy { position: absolute; left: 27px; top: 298px; width: 320px; font-size: 16px; line-height: 1.3; color: var(--brown); }
  .rate-example { position: absolute; left: 27px; top: 349px; font-size: 16px; color: var(--brown); display: flex; align-items: center; gap: 12px; }
  .rate-tag { position: relative; background: var(--red); color: var(--white); font-size: 15px; padding: 3px 10px 3px 11px; word-spacing: 4px; }
  .rate-tag::before { content: ""; position: absolute; left: -6px; top: 50%; margin-top: -6px; border: 6px solid transparent; border-left: 0; border-right-color: var(--red); }
  .rate-ps { position: absolute; left: 27px; top: 467px; width: 320px; font-size: 16px; line-height: 1.3; color: var(--brown); }

  /* Footer */
  .footer-wave { position: absolute; left: 0; bottom: 0; width: 1200px; height: 230px; }
  .footer-terms { position: absolute; left: 849px; top: 729px; color: var(--white); font-size: 11px; line-height: 1.4; }
  .brand { position: absolute; left: 1012px; top: 758px; display: flex; align-items: center; gap: 8px; }
  .brand-mark { width: 14px; height: 14px; background: var(--red); border: 1px solid var(--white); }
  .brand-name { color: var(--white); font-size: 30px; font-weight: 700; line-height: 1; }
</style>
</head>
<body>
<main class="tent">

  <section class="side side--win">
    <div class="win-block">
      <div class="win-emblem"></div>
      <div class="win-greens win-greens--left" role="img" aria-label="Fresh salad leaves"></div>
      <div class="win-greens win-greens--right" role="img" aria-label="Fresh salad leaves"></div>
      <p class="win-lead">Rate your waiter and</p>
      <p class="win-chance">Stand a chance to</p>
      <p class="win-big">Win</p>
      <svg class="win-cloche" viewBox="0 0 58 42" aria-hidden="true">
        <circle cx="29" cy="7" r="3" fill="#1a1a1a"/>
        <path d="M8 28 A21 19 0 0 1 50 28 Z" fill="#1a1a1a"/>
        <rect x="4" y="29" width="50" height="4" rx="2" fill="#1a1a1a"/>
        <path d="M20 33 L26 42 L34 42 L30 33 Z" fill="#1a1a1a"/>
      </svg>
      <p class="win-meal">A FREE MEAL</p>
      <p class="win-for">for 2</p>
    </div>
  </section>

  <section class="side side--hear">
    <p class="hear-intro">We love our customers<br>and want to hear from you.</p>
    <p class="hear-headline">Good or bad,<span>we want to know.</span></p>
    <p class="hear-ps"><small>P.S.</small>It's 100% anonymous.</p>
  </section>

  <section class="side side--rate">
    <svg class="rate-medal" viewBox="0 0 124 150" aria-hidden="true">
      <path d="M44 100 L44 150 L62 136 L80 150 L80 100 Z" fill="var(--brown)"/>
      <circle cx="62" cy="58" r="58" fill="var(--brown)"/>
      <circle cx="62" cy="58" r="50" fill="none" stroke="#e9dcd8" stroke-width="1.5" stroke-dasharray="2 2"/>
      <circle cx="62" cy="32" r="3" fill="#fff"/>
      <path d="M38 58 A24 22 0 0 1 86 58 Z" fill="#fff"/>
      <rect x="34" y="59" width="56" height="4" rx="2" fill="#fff"/>
      <path d="M50 63 L56 80 L64 80 L60 63 Z" fill="#fff"/>
    </svg>
    <h2 class="rate-title">Rate your waiter:</h2>
    <p class="rate-copy">SMS your waiter's badge number and score out of 10 to 48216</p>
    <p class="rate-example">Example: <span class="rate-tag">99812 9</span></p>
    <p class="rate-ps">P.S. We hate spam. You will not be added to any mailing list.</p>
  </section>

  <svg class="footer-wave" viewBox="0 0 1200 230" preserveAspectRatio="none" aria-hidden="true">
    <defs>
      <linearGradient id="waveRed" x1="0" y1="0" x2="1" y2="0">
        <stop offset="0" stop-color="#a2141c"/>
        <stop offset=".55" stop-color="#8c1117"/>
        <stop offset="1" stop-color="var(--red-deep)"/>
      </linearGradient>
    </defs>
    <path d="M0 120 C180 150 330 215 540 200 C760 185 950 40 1200 20 L1200 230 L0 230 Z" fill="#d8323a"/>
    <path d="M0 140 C190 165 340 225 560 210 C770 195 960 65 1200 42 L1200 230 L0 230 Z" fill="url(#waveRed)"/>
  </svg>
  <p class="footer-terms">Terms and conditions apply. R3 per SMS.<br>Brought to you by plumo.co.za</p>
  <div class="brand">
    <span class="brand-mark"></span>
    <span class="brand-name">Plumo</span>
  </div>

</main>
</body>
</html>
```